Banner to be displayed at local Farmers Market Booth.

Graphic Design Brief: Farmers Market Banner Contest

Project Overview:We are seeking talented graphic designers to create a visually appealing banner for our booth at the local farmers market. Our company specializes in healthy, all-natural dog and cat treats, and we want a banner that captures our brand identity while drawing in pet owners who value quality and nutrition for their furry friends.

Banner Specifications:

Size: 24 inches x 60 inches (Horizontal orientation) 24" High X 60 wide

Theme: Vintage/Retro

Style: Warm, inviting, nostalgic with a touch of rustic charm

Colors: Earthy, muted tones such as warm browns, soft greens, and creamy yellows. Pops of red or blue may be used sparingly for accents. OR Black and White with gray scales. Would like to see both

Typography: Retro-style fonts that are readable and align with the vintage aesthetic.

Key Elements to Include: website (www.tobyssupreme.net)

Company Name: Toby's Supreme

Tagline: " Just Good Stuff "
Imagery: Illustrations or stylized graphics of happy dogs and cats, possibly interacting with treats.

Emphasis on Natural Ingredients: Icons or design elements that subtly suggest freshness and quality (e.g., leaves, wheat, bones, or paw prints).

Farmers Market Appeal: A design that blends well with the artisanal, handmade, and farm-fresh atmosphere of the market.

Design Considerations:

The banner should be easily readable from a distance.

A balanced composition that doesn't feel overcrowded.

Should evoke trust and warmth while maintaining a professional look.

Avoid overly modern or sleek elements that don’t align with the vintage aesthetic.

Submission Requirements:

High-resolution digital file in PDF or AI format.

CMYK color mode for printing purposes.

Must include a mockup or preview of how it would look in a real farmers market setting.

We look forward to seeing your creative interpretations of our brand! If you have any questions, feel free to reach out.

Font styles to use
Other font styles liked:

Requirements
Nice to have
• Retro/Vintage,playful BUT NOT whimsical

```html
<!DOCTYPE html>
<html lang="en">
<head>
<meta charset="utf-8">
<title>Toby's Supreme – Just Good Stuff Banner</title>
<link href="https://fonts.googleapis.com/css2?family=Black+Ops+One&family=Libre+Baskerville:wght@400;700&display=swap" rel="stylesheet">
<style>
  :root {
    --ink: #141414;
    --paper: #f1efea;
    --mustard: #ece84a;
    --stage: #e4e2dc;
    --engraving: #a9a7a2;
  }
  html, body {
    margin: 0;
    padding: 0;
    width: 1200px;
    height: 944px;
    overflow: hidden;
    background: var(--stage);
  }
  .banner {
    position: absolute;
    left: 0;
    top: 232px;
    width: 1200px;
    height: 480px;
    background: var(--mustard);
    overflow: hidden;
  }
  .banner__shapes {
    position: absolute;
    inset: 0;
  }
  .tagline {
    position: absolute;
    left: 56px;
    top: 68px;
    margin: 0;
    font-family: "Black Ops One", "Arial Black", sans-serif;
    font-weight: 400;
    font-size: 112px;
    line-height: 108px;
    letter-spacing: 2px;
    color: var(--ink);
    text-transform: uppercase;
  }
  .website {
    position: absolute;
    left: 96px;
    top: 420px;
    width: 440px;
    text-align: center;
    font-family: "Libre Baskerville", Georgia, serif;
    font-weight: 700;
    font-size: 17px;
    letter-spacing: 3px;
    color: var(--ink);
  }
  .pet-portrait {
    position: absolute;
    left: 468px;
    top: 14px;
    width: 222px;
    height: 222px;
    border-radius: 50%;
    border: 5px solid var(--ink);
    box-sizing: border-box;
    background: radial-gradient(circle at 55% 45%, #f3f2ef 0%, #c9c7c2 60%, var(--engraving) 100%);
  }
  .brand {
    position: absolute;
    left: 712px;
    top: 52px;
    margin: 0;
    font-family: "Libre Baskerville", Georgia, serif;
    font-weight: 400;
    color: var(--ink);
    text-transform: uppercase;
  }
  .brand__first {
    display: block;
    font-size: 62px;
    line-height: 80px;
  }
  .brand__second {
    display: block;
    font-size: 54px;
    line-height: 74px;
    padding-left: 14px;
  }
  .brand-mark {
    position: absolute;
    left: 1020px;
    top: 36px;
    display: flex;
    align-items: center;
    gap: 8px;
    font-family: "Libre Baskerville", Georgia, serif;
    font-size: 22px;
    color: var(--ink);
  }
  .brand-mark__dot {
    width: 18px;
    height: 18px;
    border-radius: 50%;
    border: 2px solid var(--ink);
    box-sizing: border-box;
  }
  .offer {
    position: absolute;
    left: 712px;
    top: 252px;
    margin: 0;
    font-family: "Libre Baskerville", Georgia, serif;
    font-weight: 400;
    font-size: 40px;
    line-height: 58px;
    color: var(--ink);
    text-transform: uppercase;
    white-space: nowrap;
  }
</style>
</head>
<body>
  <section class="banner">
    <svg class="banner__shapes" width="1200" height="480" viewBox="0 0 1200 480" aria-hidden="true">
      <polygon class="panel-dark-edge" fill="#141414"
        points="0,0 590,0 584,40 596,70 590,110 600,150 592,190 604,240 596,290 606,330 596,370 604,410 598,450 602,480 0,480"/>
      <polygon class="panel-white" fill="#f1efea"
        points="16,18 578,14 572,52 584,78 578,116 588,154 580,192 592,240 584,290 594,330 584,370 592,408 586,446 16,462 12,300 20,150"/>
    </svg>

    <h1 class="tagline">Just<br>Good<br>Stuff</h1>
    <div class="website">WWW.TOBYSSUPREME.NET</div>

    <div class="pet-portrait" role="img" aria-label="Engraved vintage illustration of a dog and a cat sitting together"></div>

    <h2 class="brand">
      <span class="brand__first">Toby's</span>
      <span class="brand__second">Supreme</span>
    </h2>
    <div class="brand-mark"><span class="brand-mark__dot"></span>Toby's</div>

    <p class="offer">Purveyors of<br>Premium Pet<br>Food &amp; Treats</p>
  </section>
</body>
</html>
```